Smart, intuitive SaaS software dashboard design

PactLoom is an innovative modern SaaS (software as a service) solution for contract and meeting management.

What we are looking for is fresh ideas for our dashboard. We do not need web coding or actionable wireframes now – but purely great design ideas from where to continue forward.

How should a modern web software dashboard look like? Fresh, intuitive, easy-to-use, and adaptable for responsive mobile designs. We hope that when the user logs into the service and sees the dashboard, he/she gets a good big picture of the current status of the most important documents of his/hers company.

To get to know the service and see the components, we kindly ask you to register to our service at www.pactloom-example.net and to utilize the free trial (30 days) so you can see the existing dashboard live. And also try out how it works. Might help you to get ideas how to improve it.

(The designer we will choose might be offered later on to design some other pages as well (contract view and edit pages, meeting page etc).)

You’ll find additional information in the attachment.

You’ll find more information of the company and the service also at www.pactloom-example.net

Target Market(s)

Global

Industry/Entity Type

Business Management

Number of Pages Required

1 page

Font styles to use
Sans Serif

Requirements
Must have
• 1) Clear design idea for us to iterate from, 2) Modern look and feel - elegant & bold at the same time - still with credibility in our target group. And 3) Suitable for dashboard usage - it should it a clear big picture for the user.
• UPDATE:
• Users should see most important things with one glance. Therefore we would like to see AT LEAST these items mentioned below on the first page.
• NOTE: if all these things are visible on the dashboard, the menu list is maybe not needed on the left. (And there might be some icons on the top header with needed settings/inbox features anyway.)
• NOTE2: as explained earlier, the design should be responsive i.e. work without modifications in PC, iPad and mobile (the areas/boxes would just rearrange themselves on top of each other.)
• -First area should be Documents, which would include different document categories: Contracts, Finance & Admin and HR
• -All different types of Meetings could be the next area (upcoming ones clearly visible with date and maybe description, time and location visible also).
• -Reminders and Activity Feed (they might also be together in top of each other, so that Reminder is visible first and Activity feed can be chosen from the tab.)
• -Virtual Datarooms (maybe 1-3 different ones with some analytics for each visible e.g. like usage/visits per day)
• Saved searches in very important list as users can save their most important searches. There are typically many of these, so at least 5 should be visible and then see all button (maybe even more could be visible if they fit on your design)
• My Latest is also important.
• (As explained, Action Required area is NOT needed anymore).
Nice to have
• Surprise us!
Should not have
• Please avoid the boring traditional legacy stuff and the common report dashboards.
• You do not need design a 100% mockup for the techie to continue with. The ideas count.

```html
<!DOCTYPE html>
<html lang="en">
<head>
<meta charset="utf-8">
<title>PactLoom Dashboard</title>
<link rel="stylesheet" href="https://fonts.googleapis.com/css2?family=Open+Sans:ital,wght@0,300;0,400;0,600;0,700;1,600&display=swap">
<style>
:root{
  --blue:#2f7bc4;
  --blue-deep:#2a6fb3;
  --blue-light:#3b8bd6;
  --blue-text:#2a78c5;
  --blue-soft:#cfe2f5;
  --green:#7dc242;
  --green-text:#5cab2d;
  --orange:#f5a33b;
  --pink:#e8436a;
  --ink:#222;
  --muted:#8a8a8a;
  --line:#e3e3e3;
  --row-alt:#f1f1f1;
  --black:#000;
  --white:#fff;
}
*{box-sizing:border-box;margin:0;padding:0}
html,body{width:1200px;height:900px;overflow:hidden}
body{font-family:"Open Sans",Arial,sans-serif;color:var(--ink);position:relative;
  background:linear-gradient(135deg,#2a74bd 0%,#3584cf 45%,#2c77c2 100%)}
svg{display:block}

/* ---------- top bar ---------- */
.brand{position:absolute;left:0;top:0;width:262px;height:86px;background:var(--black);
  display:flex;align-items:center;padding-left:30px;gap:10px}
.brand-dot{width:34px;height:34px;border-radius:50%;background:var(--green)}
.brand-name{color:var(--white);font-size:20px;font-weight:600;letter-spacing:.5px}
.topbar{position:absolute;left:262px;top:0;right:0;height:86px;display:flex;align-items:center;padding:0 18px 0 36px;color:var(--white)}
.scope{font-style:italic;font-weight:600;font-size:16px;display:flex;align-items:center;gap:8px;padding-right:12px;border-right:1px solid rgba(255,255,255,.35);height:26px}
.search{width:390px;height:26px;margin-left:10px;border-bottom:1px solid rgba(255,255,255,.45);display:flex;align-items:center;justify-content:space-between;color:rgba(255,255,255,.55);font-size:13px}
.add-btn{margin-left:28px}
.greeting{margin-left:auto;font-size:15px;display:flex;align-items:center;gap:6px}
.greeting b{font-weight:700}
.avatar{width:48px;height:48px;border-radius:50%;background:#e6e6e6;margin:0 18px 0 12px}
.logout{font-size:15px;display:flex;align-items:center;gap:6px}

/* ---------- sidebar ---------- */
.sidebar{position:absolute;left:0;top:86px;width:262px;bottom:50px;
  background:linear-gradient(180deg,#2f7dc7,#2b74bd)}
.nav-item{height:60px;display:flex;align-items:center;padding:0 26px;gap:16px;color:var(--white);font-size:17px;
  border-bottom:1px solid rgba(0,0,0,.12);box-shadow:0 1px 0 rgba(255,255,255,.08)}
.nav-item .caret{margin-left:auto}
.nav-open{background:rgba(0,0,0,.08)}
.saved-list{list-style:none;background:rgba(0,0,0,.1);padding:6px 0 8px}
.saved-list li{height:33px;display:flex;align-items:center;gap:10px;padding-left:60px;color:var(--white);font-size:14px}
.saved-list li::before{content:"";width:5px;height:5px;border-radius:50%;background:var(--green)}
.saved-list .see-all{color:#bfe0ff;font-weight:600;font-size:13px}
.saved-list .see-all::before{display:none}

/* ---------- cards ---------- */
.card{position:absolute;background:var(--white);overflow:hidden}
.card-head{height:52px;display:flex;align-items:center;padding:0 16px;gap:12px;font-size:25px;font-weight:300}
.head-green{background:var(--green);color:var(--white)}
.head-blue{background:var(--blue-deep);color:var(--white)}
.head-white{color:var(--ink);border-bottom:1px solid var(--line)}
.close{position:absolute;width:12px;height:12px;border-radius:50%;background:#c9c9c9}
.close::before,.close::after{content:"";position:absolute;left:3px;top:5.5px;width:6px;height:1.2px;background:#fff;transform:rotate(45deg)}
.close::after{transform:rotate(-45deg)}
.scroll{position:absolute;width:4px;background:#d0d0d0;border-radius:2px}
.meta{font-size:12px;font-weight:700;color:var(--muted);margin-top:2px}
.meta .loc{color:var(--green-text)}
.meta .time{color:var(--blue-text)}
.title{font-size:14.5px}

/* activity feed */
.activity{left:275px;top:97px;width:348px;height:423px}
.feed-row{position:relative;height:73px;display:flex;align-items:center;padding:0 18px}
.date{width:44px}
.date .day{font-size:22px;font-weight:400;line-height:1}
.date .mon{font-size:14px;color:var(--muted)}
.feed-body{border-left:1px solid #ccc;padding-left:12px;flex:1;height:46px;display:flex;flex-direction:column;justify-content:center}
.tag{position:absolute;right:18px;bottom:10px;font-size:11.5px;color:var(--white);padding:1px 5px;font-weight:600}
.tag-done{background:var(--green)}
.tag-upload{background:var(--orange)}
.tag-login{background:var(--blue-light)}
.tag-out{background:#9b9b9b}

/* virtual datarooms */
.datarooms{left:636px;top:97px;width:552px;height:423px}
.badges{margin-left:auto;display:flex;font-size:12px;font-weight:600}
.badge-count{background:var(--orange);color:var(--white);padding:6px 10px}
.badge-all{background:var(--blue-deep);color:var(--white);padding:6px 10px}
.room-row{position:relative;height:123px;margin:0 24px 0 18px;display:flex;align-items:center;border-bottom:1px solid var(--line)}
.room-row:last-child{border-bottom:0}
.room-icon{width:40px}
.room-info{width:210px}
.room-info .title{font-weight:600}
.room-chart{flex:1;height:78px;display:flex;flex-direction:column;justify-content:flex-end;border-left:1px solid var(--line);border-right:1px solid var(--line);padding:0 14px}
.room-chart .days{display:flex;justify-content:space-between;font-size:10px;color:var(--muted);margin-top:3px}
.visits{width:110px;padding-left:16px}
.visits .num{font-size:30px;font-weight:300;color:#333;line-height:1.1}
.visits .lbl{color:var(--blue-text);font-size:13px}

/* my latest */
.latest{left:275px;top:532px;width:348px;height:318px}
.latest-row{height:66px;display:flex;align-items:center;padding:0 14px;gap:16px}
.latest-row:nth-child(even){background:var(--row-alt)}

/* meetings */
.meetings{left:636px;top:532px;width:361px;height:318px}
.meet-row{position:relative;height:86px;margin:0 14px;display:flex;align-items:center;border-bottom:1px solid var(--line)}
.meet-row .icon{width:42px;padding-left:18px}
.duration{width:120px;font-size:24px;font-weight:300;color:#333;border-right:1px solid var(--line);height:50px;display:flex;align-items:center;gap:5px;padding-left:12px}
.duration small{font-size:14px;color:#555}
.meet-info{padding-left:13px}
.meet-info .title{color:#555}
.meet-info .meta{color:#333}

/* reminder */
.reminder{left:1011px;top:532px;width:177px;height:318px}
.rem-row{position:relative;height:80px;margin:0 14px 0 18px;border-bottom:1px solid var(--line);padding-top:12px}
.rem-date{display:flex;align-items:center;gap:6px;font-size:22px}
.rem-date small{font-size:14px;color:#555}
.rem-row .what{font-size:14px;font-weight:600;color:#555;margin-top:2px}

/* footer */
.footer{position:absolute;left:0;right:0;bottom:0;height:50px;background:var(--black);display:flex;align-items:center;padding:0 28px;font-size:12px;color:#444}
.seal{width:46px;height:20px;border-radius:3px;background:#f0c419;margin-right:20px}
.footer .legal{margin-left:auto}
</style>
</head>
<body>

<svg width="0" height="0" style="position:absolute">
  <defs>
    <symbol id="i-chart" viewBox="0 0 20 16"><rect x="1" y="10" width="3" height="6" fill="currentColor"/><rect x="6" y="7" width="3" height="9" fill="currentColor"/><rect x="11" y="9" width="3" height="7" fill="currentColor"/><rect x="16" y="4" width="3" height="12" fill="currentColor"/><path d="M1 8 L7 4 L12 6 L19 1" stroke="currentColor" stroke-width="1.6" fill="none"/></symbol>
    <symbol id="i-cup" viewBox="0 0 20 16"><path d="M3 3 H14 V9 A4 4 0 0 1 10 13 H7 A4 4 0 0 1 3 9 Z" fill="currentColor"/><path d="M14 5 H16 A2 2 0 0 1 16 9 H14" stroke="currentColor" stroke-width="1.6" fill="none"/><rect x="1" y="14" width="16" height="2" fill="currentColor"/></symbol>
    <symbol id="i-doc" viewBox="0 0 16 18"><rect x="1" y="1" width="14" height="16" rx="2" stroke="currentColor" stroke-width="1.8" fill="none"/><path d="M4 6 H12 M4 9 H12 M4 12 H12" stroke="currentColor" stroke-width="1.6"/></symbol>
    <symbol id="i-cal" viewBox="0 0 18 18"><rect x="1" y="3" width="16" height="14" rx="2" fill="currentColor"/><rect x="4" y="0" width="2" height="5" fill="currentColor"/><rect x="12" y="0" width="2" height="5" fill="currentColor"/><g fill="#fff"><rect x="4" y="8" width="2.5" height="2.5"/><rect x="8" y="8" width="2.5" height="2.5"/><rect x="12" y="8" width="2.5" height="2.5"/><rect x="4" y="12" width="2.5" height="2.5"/><rect x="8" y="12" width="2.5" height="2.5"/></g></symbol>
    <symbol id="i-room" viewBox="0 0 22 20"><path d="M2 4 H9 L11 6 H20 V18 H2 Z" fill="currentColor"/><rect x="9" y="10" width="5" height="5" rx="1" fill="#fff"/></symbol>
    <symbol id="i-caret" viewBox="0 0 12 8"><path d="M0 0 H12 L6 7 Z" fill="currentColor"/></symbol>
  </defs>
</svg>

<div class="brand"><span class="brand-dot"></span><span class="brand-name">PACTLOOM</span></div>

<header class="topbar">
  <div class="scope">Contracts <svg width="12" height="8"><use href="#i-caret" color="#fff"/></svg></div>
  <div class="search">Search
    <svg width="18" height="18" viewBox="0 0 18 18"><circle cx="7.5" cy="7.5" r="6" stroke="#fff" stroke-width="1.5" fill="none"/><path d="M12 12 L17 17" stroke="#fff" stroke-width="1.5"/></svg>
  </div>
  <svg class="add-btn" width="24" height="24" viewBox="0 0 24 24"><circle cx="12" cy="12" r="12" fill="#fff"/><path d="M12 6 V18 M6 12 H18" stroke="#2f7bc4" stroke-width="3"/></svg>
  <div class="greeting"><b>Hi,</b> Brightwell</div>
  <div class="avatar" role="img" aria-label="User avatar"></div>
  <div class="logout"><svg width="12" height="14" viewBox="0 0 12 14"><path d="M3 6 V4 A3 3 0 0 1 9 4 V6" stroke="#fff" stroke-width="1.8" fill="none"/><rect x="1" y="6" width="10" height="8" rx="1" fill="#fff"/></svg>logout</div>
</header>

<nav class="sidebar">
  <div class="nav-item"><svg width="18" height="20" viewBox="0 0 16 18" color="#fff"><use href="#i-doc"/></svg>Contracts</div>
  <div class="nav-item"><svg width="20" height="16" color="#fff"><use href="#i-chart"/></svg>Finance &amp; Admin</div>
  <div class="nav-item"><svg width="18" height="18" viewBox="0 0 18 18"><circle cx="8" cy="8" r="6.5" stroke="#fff" stroke-width="2" fill="none"/><circle cx="8" cy="6.5" r="2" fill="#fff"/><path d="M4.5 11.5 A3.5 3 0 0 1 11.5 11.5" fill="#fff"/><path d="M13 13 L17 17" stroke="#fff" stroke-width="2.4"/></svg>HR</div>
  <div class="nav-item"><svg width="18" height="20" viewBox="0 0 16 18" color="#fff"><use href="#i-doc"/></svg>Company Register</div>
  <div class="nav-item"><svg width="20" height="16" color="#fff"><use href="#i-cup"/></svg>Meetings<svg class="caret" width="12" height="8" color="#8fc3f0"><use href="#i-caret"/></svg></div>
  <div class="nav-item nav-open"><svg width="18" height="18" viewBox="0 0 18 18"><circle cx="8" cy="8" r="6.5" stroke="#fff" stroke-width="2" fill="none"/><path d="M8 5 V11 M5 8 H11" stroke="#fff" stroke-width="1.6"/><path d="M13 13 L17 17" stroke="#fff" stroke-width="2.4"/></svg>Saved Searches<svg class="caret" width="12" height="8" color="#8fc3f0"><use href="#i-caret"/></svg></div>
  <ul class="saved-list">
    <li>Contracts ending in 30 days</li>
    <li>Unsigned NDAs</li>
    <li>Board minutes 2016</li>
    <li>Open invoices over 5k</li>
    <li>New hire agreements</li>
    <li class="see-all">See all searches ›</li>
  </ul>
</nav>

<!-- Activity Feed -->
<section class="card activity">
  <div class="card-head head-green"><svg width="24" height="22" viewBox="0 0 24 22"><rect width="24" height="22" rx="3" fill="#fff"/><path d="M5 6 H19 M5 11 H19 M5 16 H19" stroke="#7dc242" stroke-width="2.4"/></svg>Activity Feed</div>
  <span class="scroll" style="right:10px;top:70px;height:60px"></span>
  <div class="feed-row"><span class="close" style="right:22px;top:7px"></span><div class="date"><div class="day">22</div><div class="mon">May</div></div><div class="feed-body"><div class="title">Lorem ipsum dolor sit ipsum ame,</div><div class="meta">10.30 am, 2016 | <span class="loc">USA</span></div></div><span class="tag tag-done">Finished...</span></div>
  <div class="feed-row"><span class="close" style="right:22px;top:7px"></span><div class="date"><div class="day">21</div><div class="mon">May</div></div><div class="feed-body"><div class="title">Lorem ipsum dolor sit amet,</div><div class="meta">09.30 am, 2016 | <span class="loc">USA</span></div></div><span class="tag tag-upload">UpLoad...</span></div>
  <div class="feed-row"><span class="close" style="right:22px;top:7px"></span><div class="date"><div class="day">20</div><div class="mon">May</div></div><div class="feed-body"><div class="title">Lorem ipsum dolor sit ipsum ame,</div><div class="meta">10.30 am, 2016 | <span class="loc">USA</span></div></div><span class="tag tag-login">Login...</span></div>
  <div class="feed-row"><span class="close" style="right:22px;top:7px"></span><div class="date"><div class="day">20</div><div class="mon">May</div></div><div class="feed-body"><div class="title">Lorem ipsum dolor sit amet,</div><div class="meta">09.30 am, 2016 | <span class="loc">USA</span></div></div><span class="tag tag-out">Log out</span></div>
  <div class="feed-row"><span class="close" style="right:22px;top:7px"></span><div class="date"><div class="day">19</div><div class="mon">May</div></div><div class="feed-body"><div class="title">Lorem ipsum dolor sit ipsum ame,</div><div class="meta">10.30 am, 2016 | <span class="loc">USA</span></div></div><span class="tag tag-upload">UpLoad...</span></div>
</section>

<!-- Virtual Datarooms -->
<section class="card datarooms">
  <div class="card-head head-white"><svg width="24" height="22" viewBox="0 0 22 20" color="#e8436a"><use href="#i-room"/></svg>Virtual Datarooms
    <div class="badges"><span class="badge-count">3 ROOMS</span><span class="badge-all">See all</span></div>
  </div>
  <div>
    <div class="room-row"><span class="close" style="right:0;top:12px"></span><div class="room-icon"><svg width="22" height="20" viewBox="0 0 22 20" color="#f5a33b"><use href="#i-room"/></svg></div><div class="room-info"><div class="title">Acquisition Due Diligence</div><div class="meta">24 members | <span class="loc">Active</span></div></div>
      <div class="room-chart"><svg width="190" height="52" viewBox="0 0 190 52"><g fill="#f5a33b"><rect x="4" y="30" width="18" height="22"/><rect x="31" y="18" width="18" height="34"/><rect x="58" y="24" width="18" height="28"/><rect x="85" y="10" width="18" height="42"/><rect x="112" y="20" width="18" height="32"/><rect x="139" y="36" width="18" height="16"/><rect x="166" y="6" width="18" height="46"/></g></svg><div class="days"><span>M</span><span>T</span><span>W</span><span>T</span><span>F</span><span>S</span><span>S</span></div></div>
      <div class="visits"><div class="num">48</div><div class="lbl">visits today</div></div></div>
    <div class="room-row"><span class="close" style="right:0;top:12px"></span><div class="room-icon"><svg width="22" height="20" viewBox="0 0 22 20" color="#7dc242"><use href="#i-room"/></svg></div><div class="room-info"><div class="title">Board Materials 2016</div><div class="meta">9 members | <span class="loc">Active</span></div></div>
      <div class="room-chart"><svg width="190" height="52" viewBox="0 0 190 52"><g fill="#7dc242"><rect x="4" y="36" width="18" height="16"/><rect x="31" y="28" width="18" height="24"/><rect x="58" y="40" width="18" height="12"/><rect x="85" y="22" width="18" height="30"/><rect x="112" y="30" width="18" height="22"/><rect x="139" y="44" width="18" height="8"/><rect x="166" y="26" width="18" height="26"/></g></svg><div class="days"><span>M</span><span>T</span><span>W</span><span>T</span><span>F</span><span>S</span><span>S</span></div></div>
      <div class="visits"><div class="num">17</div><div class="lbl">visits today</div></div></div>
    <div class="room-row"><span class="close" style="right:0;top:12px"></span><div class="room-icon"><svg width="22" height="20" viewBox="0 0 22 20" color="#2f7bc4"><use href="#i-room"/></svg></div><div class="room-info"><div class="title">Investor Relations</div><div class="meta">31 members | <span class="loc">Active</span></div></div>
      <div class="room-chart"><svg width="190" height="52" viewBox="0 0 190 52"><g fill="#2f7bc4"><rect x="4" y="20" width="18" height="32"/><rect x="31" y="26" width="18" height="26"/><rect x="58" y="12" width="18" height="40"/><rect x="85" y="16" width="18" height="36"/><rect x="112" y="8" width="18" height="44"/><rect x="139" y="38" width="18" height="14"/><rect x="166" y="32" width="18" height="20"/></g></svg><div class="days"><span>M</span><span>T</span><span>W</span><span>T</span><span>F</span><span>S</span><span>S</span></div></div>
      <div class="visits"><div class="num">62</div><div class="lbl">visits today</div></div></div>
  </div>
</section>

<!-- My Latest -->
<section class="card latest">
  <div class="card-head head-blue"><svg width="34" height="22" viewBox="0 0 34 22"><rect width="24" height="22" rx="2" fill="#fff"/><circle cx="8" cy="9" r="3" fill="#2a6fb3"/><path d="M3 17 A5 4 0 0 1 13 17 Z" fill="#2a6fb3"/><path d="M15 7 H21 M15 11 H21" stroke="#2a6fb3" stroke-width="2"/><rect x="26" y="0" width="3" height="22" fill="#fff"/><rect x="31" y="0" width="3" height="22" fill="#fff"/></svg>My Latest</div>
  <span class="scroll" style="right:20px;top:62px;height:50px"></span>
  <div>
    <div class="latest-row"><svg width="20" height="16" color="#f5a33b"><use href="#i-chart"/></svg><div><div class="title">Lorem ipsum dolor sit ipsum amet,</div><div class="meta"><span class="time">10.30 am,</span> 2016 | <span class="loc">USA</span></div></div></div>
    <div class="latest-row"><svg width="20" height="16" color="#7dc242"><use href="#i-cup"/></svg><div><div class="title">Lorem ipsum dolor sit ipsum ametipum.</div><div class="meta"><span class="time">10.30 am,</span> 2016 | <span class="loc">USA</span></div></div></div>
    <div class="latest-row"><svg width="20" height="18" viewBox="0 0 16 18" color="#2f7bc4"><use href="#i-doc"/></svg><div><div class="title">Lorem ipsum dolor sit ipsum amet,</div><div class="meta"><span class="time">10.30 am,</span> 2016 | <span class="loc">USA</span></div></div></div>
    <div class="latest-row"><svg width="20" height="16" color="#7dc242"><use href="#i-cup"/></svg><div><div class="title">Lorem ipsum dolor sit ipsum eti apsum.</div><div class="meta"><span class="time">10.30 am,</span> 2016 | <span class="loc">USA</span></div></div></div>
  </div>
</section>

<!-- Meetings -->
<section class="card meetings">
  <div class="card-head head-white"><svg width="30" height="22" viewBox="0 0 30 22"><circle cx="10" cy="6" r="5" fill="#f5a33b"/><path d="M0 22 A10 9 0 0 1 20 22 Z" fill="#f5a33b"/><circle cx="21" cy="6" r="4" fill="#f5a33b"/><path d="M17 13 A8 8 0 0 1 30 22 H22 A11 10 0 0 0 17 13 Z" fill="#f5a33b"/></svg>Meetings</div>
  <div>
    <div class="meet-row"><span class="close" style="right:0;top:8px"></span><div class="icon"><svg width="20" height="16" color="#f5a33b"><use href="#i-cup"/></svg></div><div class="duration">40.00 <small>min</small></div><div class="meet-info"><div class="title">Lorem ipsum dolor sit</div><div class="meta">25 MAY, 2016 | <span class="loc">USA</span></div></div></div>
    <div class="meet-row"><span class="close" style="right:0;top:8px"></span><div class="icon"><svg width="20" height="16" color="#2f7bc4"><use href="#i-cup"/></svg></div><div class="duration">01.00 <small>hr</small></div><div class="meet-info"><div class="title">Lorem ipsum dolor sit</div><div class="meta">25 MAY, 2016 | <span class="loc">Canada</span></div></div></div>
    <div class="meet-row" style="border-bottom:0"><span class="close" style="right:0;top:8px"></span><div class="icon"><svg width="20" height="16" color="#2f7bc4"><use href="#i-cup"/></svg></div><div class="duration">02.00 <small>hr</small></div><div class="meet-info"><div class="title">Lorem ipsum dolor sit</div><div class="meta">25 MAY, 2016 | <span class="loc">USA</span></div></div></div>
  </div>
</section>

<!-- Reminder -->
<section class="card reminder">
  <div class="card-head head-blue"><svg width="26" height="26" viewBox="0 0 26 26"><path d="M4 13 A9 9 0 1 0 7 6" stroke="#fff" stroke-width="2.4" fill="none"/><path d="M3 2 V8 H9" stroke="#fff" stroke-width="2.4" fill="none"/><path d="M13 8 V13 L17 16" stroke="#fff" stroke-width="2.2" fill="none"/></svg>Reminder</div>
  <span class="scroll" style="right:6px;top:62px;height:50px"></span>
  <div class="rem-row"><span class="close" style="right:0;top:10px"></span><div class="rem-date"><svg width="18" height="18" color="#e8436a"><use href="#i-cal"/></svg>25 <small>may</small></div><div class="what">Board Meetng</div></div>
  <div class="rem-row"><span class="close" style="right:0;top:10px"></span><div class="rem-date"><svg width="18" height="18" color="#f5a33b"><use href="#i-cal"/></svg>26 <small>may</small></div><div class="what">Board Meetng</div></div>
  <div class="rem-row" style="border-bottom:0"><span class="close" style="right:0;top:10px"></span><div class="rem-date"><svg width="18" height="18" color="#f5a33b"><use href="#i-cal"/></svg>28 <small>may</small></div><div class="what">Board Meetng</div></div>
</section>

<footer class="footer">
  <span class="seal"></span>
  <span>Copyright © 2016 PactLoom Ltd</span>
  <span class="legal">Terms of Use Privacy</span>
</footer>

</body>
</html>
```